依頼詳細
クリニックのHPです。
https://kitase-naika.jp
チラシはA4サイズです。
自分のイメージとして、こんなチラシが好き、こんなのは嫌という例を添付しますので参考にしてください。
添付した資料は全部使う必要はありません(特に、外観、内観予想図)。
ソノワで印刷しますので、ソノワが対応しているデータ形式でお願いします(ソノワにデータ作成テンプレートがあります)。
https://sonowa.com/guide/how-to-make-data/pamphlet/
クリニックがまだできていないので、外観予想図、内観予想図を添付します。
クリニック用のリーフレットデザインも別コンペで募集しています。
記載項目
開催日 2020年5月10日土曜日、場所、地図、アクセス
サイズ
A4
ページ数
片面
希望イメージ
シンプル 複雑
単色 カラフル
暗い 明るい
日常 高級
遊び心 厳粛
未来的 伝統的
女性的 男性的
希望する色
黄・オレンジ系、緑系、水色系
■ 選んだ理由

全体にバランスが良く、第一印象が良かったです。

■ 提案者全員のお礼・コメント

多くの皆様に応募していただき、ありがとうございます
良いデザイン案が多く、選ぶのに苦慮しました。今後も、仕事を依頼することがあると思いますが、よろしくお願いします。

```html
<!DOCTYPE html>
<html lang="ja">
<head>
<meta charset="utf-8">
<title>桜台きたせ内科 内覧会開催</title>
<link href="https://fonts.googleapis.com/css2?family=M+PLUS+Rounded+1c:wght@500;700;800&family=Noto+Sans+JP:wght@400;500;700;900&display=swap" rel="stylesheet">
<style>
:root{
  --sky:#e3f3fb;
  --blue:#2a8fdf;
  --navy:#1d4b98;
  --box:#3aa2e6;
  --green:#7cc242;
  --ink:#333;
  --line:#9cc9ea;
  --white:#fff;
}
*{margin:0;padding:0;box-sizing:border-box}
html,body{width:846px;height:1200px;overflow:hidden}
body{font-family:"Noto Sans JP",sans-serif;color:var(--ink);background:var(--sky);position:relative}
.date{position:absolute;top:14px;left:0;width:100%;text-align:center;font-family:"M PLUS Rounded 1c",sans-serif;font-weight:800;color:var(--blue);font-size:88px;line-height:1;letter-spacing:2px}
.date small{font-size:66px}
.date .day{display:inline-block;width:74px;height:74px;border-radius:50%;background:var(--blue);color:var(--white);font-size:50px;line-height:74px;vertical-align:10px;margin-left:6px}
.clinic{position:absolute;top:110px;width:100%;text-align:center;font-weight:900;color:var(--navy);font-size:60px;letter-spacing:2px}
.event{position:absolute;top:182px;left:0;width:100%;display:flex;justify-content:center;gap:10px}
.event span{width:100px;height:94px;background:var(--box);color:var(--white);font-weight:900;font-size:70px;line-height:94px;text-align:center;border-radius:4px}
.intro{position:absolute;top:290px;left:40px;width:770px;height:100px}
.intro svg{position:absolute;left:20px;top:8px}
.intro p{position:absolute;left:170px;top:0;font-size:18px;line-height:1.75;font-weight:500}
.card{position:absolute;top:400px;width:390px;height:650px;background:var(--white);border-radius:8px;padding:16px 20px}
.card.greeting{left:30px}
.card.access{left:430px}
.card h2{display:flex;align-items:center;gap:8px;font-size:24px;font-weight:700;color:var(--navy);border-bottom:2px solid var(--line);padding-bottom:8px}
.card h2 svg{flex:none}
.photo{position:absolute;top:70px;left:20px;width:140px;height:160px;background:linear-gradient(#dbe8f0,#b8cbd8);border-radius:4px}
.bio{position:absolute;top:72px;left:176px;font-size:11px;line-height:1.75}
.bio .name{font-size:13px;margin-bottom:4px}
.bio .name b{font-size:18px}
.motto{position:absolute;top:246px;left:20px;width:350px;text-align:center;color:var(--navy);font-weight:700;font-size:18px;line-height:1.5}
.motto em{font-style:normal;font-size:26px;color:var(--blue)}
.message{position:absolute;top:330px;left:20px;width:350px;font-size:11.5px;line-height:1.9}
.addr{font-size:11px;margin:10px 0 6px}
.map{width:350px;height:230px;background:linear-gradient(#f4f8fb,#e7eff5);border:1px solid #cfdbe5}
.route{font-size:11px;line-height:1.8;margin-top:12px}
.route h3{font-size:12px;color:var(--white);background:var(--box);display:inline-block;padding:0 8px;margin-top:8px;border-radius:2px}
footer{position:absolute;left:0;top:1062px;width:846px;height:138px;background:var(--white)}
.brand{position:absolute;left:42px;top:28px;display:flex;align-items:center;gap:14px}
.brand i{width:52px;height:52px;border-radius:50%;background:var(--blue)}
.brand b{display:block;font-size:32px;font-weight:500;color:var(--navy)}
.brand small{display:block;font-size:13px;color:var(--navy);text-align:center}
.faddr{position:absolute;left:42px;top:104px;font-size:11px}
.contact{position:absolute;right:42px;top:30px;text-align:right;color:var(--navy)}
.contact .tel{font-size:36px;font-weight:700;display:flex;align-items:center;gap:6px}
.contact .url{font-size:22px;font-weight:500;color:var(--blue)}
</style>
</head>
<body>
<div class="date">5<small>月</small>10<small>日</small><span class="day">土</span></div>
<h1 class="clinic">桜台きたせ内科</h1>
<div class="event"><span>内</span><span>覧</span><span>会</span><span>開</span><span>催</span></div>

<section class="intro">
  <svg width="110" height="90" viewBox="0 0 110 90" aria-hidden="true">
    <rect x="4" y="6" width="8" height="22" fill="#2a8fdf"/><rect x="-3" y="13" width="22" height="8" fill="#2a8fdf"/>
    <rect x="28" y="30" width="46" height="56" fill="#2a8fdf"/>
    <rect x="74" y="48" width="30" height="38" fill="#1d4b98"/>
    <g fill="#fff"><rect x="36" y="40" width="10" height="10"/><rect x="56" y="40" width="10" height="10"/><rect x="36" y="58" width="10" height="10"/><rect x="56" y="58" width="10" height="10"/><rect x="82" y="58" width="14" height="8"/></g>
  </svg>
  <p>桜台きたせ内科では開院前に内覧会を行います。<br>クリニックをご自由にご見学いただけますので、<br>この機会に是非お越しください。</p>
</section>

<section class="card greeting">
  <h2><svg width="26" height="26" viewBox="0 0 26 26"><circle cx="13" cy="8" r="6" fill="#2a8fdf"/><path d="M2 26c0-7 5-11 11-11s11 4 11 11z" fill="#2a8fdf"/></svg>院長ご挨拶</h2>
  <div class="photo" role="img" aria-label="院長の写真"></div>
  <div class="bio">
    <p class="name">院長 <b>北瀬 直人</b></p>
    <p>1998年 医科大学医学部卒業</p>
    <p>1998年 大学病院内科 研修</p>
    <p>2003年 総合病院 内科勤務</p>
    <p>2010年 医学博士 取得</p>
    <p>2014年 市民病院 内科医長</p>
    <p>2020年 桜台きたせ内科 開院</p>
  </div>
  <p class="motto">地域の皆さまに寄り添う総合内科の<br><em>“かかりつけ医”</em>をめざして</p>
  <p class="message">このたび桜台の地に内科クリニックを開院する運びとなりました。これまで大学病院や地域の病院で培ってきた経験を活かし、風邪や生活習慣病など身近な症状から、専門的な検査が必要な病気まで幅広く診療いたします。患者さま一人ひとりのお話を丁寧にお聞きし、わかりやすい説明を心がけてまいります。気になることがありましたら、どうぞお気軽にご相談ください。地域の皆さまの健康を支える、身近なかかりつけ医をめざしてまいります。</p>
</section>

<section class="card access">
  <h2><svg width="24" height="28" viewBox="0 0 24 28"><path d="M12 0a10 10 0 0 0-10 10c0 8 10 18 10 18s10-10 10-18A10 10 0 0 0 12 0z" fill="#2a8fdf"/><circle cx="12" cy="10" r="4" fill="#fff"/></svg>交通案内</h2>
  <p class="addr">〒167-0000 東京都杉並区桜台1-2-3 さくらビル1F</p>
  <div class="map" role="img" aria-label="クリニック周辺の地図"></div>
  <div class="route">
    <p>最寄駅改札を出て線路沿いに徒歩約5分。<br>駐車場はございません。公共交通機関をご利用ください。</p>
    <h3>電車でお越しの方</h3>
    <p>【電車】桜台駅より徒歩5分<br>【電車】北口より徒歩7分</p>
    <h3>バスでお越しの方</h3>
    <p>【バス】桜台一丁目停留所より徒歩2分<br>【バス】桜台駅北口停留所より徒歩4分</p>
  </div>
</section>

<footer>
  <div class="brand"><i></i><div><b>桜台きたせ内科</b><small>Sakuradai Kitase Clinic</small></div></div>
  <p class="faddr">〒167-0000 東京都杉並区桜台1-2-3 さくらビル1F</p>
  <div class="contact">
    <p class="tel"><svg width="34" height="34" viewBox="0 0 24 24"><path fill="#1d4b98" d="M6.6 10.8a15 15 0 0 0 6.6 6.6l2.2-2.2a1 1 0 0 1 1-.25 11.4 11.4 0 0 0 3.6.57 1 1 0 0 1 1 1V20a1 1 0 0 1-1 1A17 17 0 0 1 3 4a1 1 0 0 1 1-1h3.5a1 1 0 0 1 1 1c0 1.25.2 2.45.57 3.57a1 1 0 0 1-.25 1z"/></svg>03-5550-0123</p>
    <p class="url">https://kitase-naika.jp/</p>
  </div>
</footer>
</body>
</html>
```